KESTREL LANE HEALTH GROUP
Modern
GORDON T PALEY
MANAGER/CEO
4172 CEDAR HOLLOW RD RENO NEVADA 89511
gpaley@kestrellanehealth.com
www.kestrellanehealth.com

```html
<!DOCTYPE html>
<html lang="en">
<head>
<meta charset="utf-8">
<title>Kestrel Lane Health Group – Stationery</title>
<link href="https://fonts.googleapis.com/css2?family=Open+Sans:wght@400;600;700&display=swap" rel="stylesheet">
<style>
:root{
  --brand:#2f86d6;
  --brand-dark:#1f6db5;
  --paper:#ffffff;
  --ink:#5a5a5a;
  --line:#d6d6d6;
  --stage:#2b2b2b;
}
*{margin:0;padding:0;box-sizing:border-box}
html,body{width:1200px;height:204px;overflow:hidden;background:var(--stage);font-family:"Open Sans",sans-serif;color:var(--ink)}
.sheet{position:absolute;background:var(--paper);overflow:hidden}
.usb,.cd{overflow:visible}
.blue{background:var(--brand);color:#fff}
.brand{display:flex;align-items:center;gap:3px;font-weight:700;color:var(--brand);white-space:nowrap;letter-spacing:.02em}
.brand i{display:block;flex:none;border-radius:50%;background:currentColor}
.blue .brand{color:#fff}
.tiny{font-size:3px;line-height:4.2px}
.card{width:60px;height:36px;padding:4px}
.card .brand{font-size:2.8px;gap:2px;letter-spacing:0}
.card .brand i{width:4px;height:4px}
.blue.card .brand{font-size:3.4px}
.card .name{font-size:3.4px;font-weight:700;margin-top:6px}
.letter{width:110px;height:156px;padding:10px 10px}
.letter .brand{font-size:5px}.letter .brand i{width:8px;height:8px}
.letter .body{margin-top:18px;font-size:2.6px;line-height:4px}
.letter .foot{position:absolute;left:0;right:0;bottom:0;height:10px;background:var(--brand);color:#fff;font-size:2.4px;padding:3px 10px;white-space:nowrap}
.dl{width:140px;height:46px;padding:6px}
.dl .brand{font-size:4.4px}.dl .brand i{width:6px;height:6px}
.stripe{position:absolute;left:0;right:0;bottom:0;height:5px;background:var(--brand)}
.usb{width:26px;height:54px;border-radius:4px;background:var(--brand);display:flex;align-items:flex-end;justify-content:center;padding-bottom:6px}
.usb::before{content:"";position:absolute;top:-10px;left:7px;width:12px;height:10px;background:#c9c9c9}
.usb i{display:block;width:8px;height:8px;border-radius:50%;background:#fff}
.folder{width:140px;height:160px;padding:14px}
.folder .brand{font-size:6px}.folder .brand i{width:10px;height:10px}
.cd{width:86px;height:86px;border-radius:50%;background:var(--brand);display:flex;align-items:center;justify-content:center}
.cd::after{content:"";width:16px;height:16px;border-radius:50%;background:var(--stage)}
</style>
</head>
<body>

<!-- business cards -->
<div class="sheet card" style="left:14px;top:40px"><div class="brand"><i></i>KESTREL LANE HEALTH GROUP</div><div class="name">GORDON T PALEY</div><div class="tiny">MANAGER/CEO</div></div>
<div class="sheet card blue" style="left:80px;top:40px;display:flex;align-items:center;justify-content:center"><div class="brand"><i></i>KESTREL LANE</div></div>
<div class="sheet card" style="left:14px;top:84px"><div class="tiny" style="font-size:2.6px;line-height:4px">4172 CEDAR HOLLOW RD RENO NEVADA 89511<br>gpaley@kestrellanehealth.com<br>www.kestrellanehealth.com</div></div>
<div class="sheet card blue" style="left:80px;top:84px;display:flex;align-items:center;justify-content:center"><div class="brand"><i></i>KESTREL LANE</div></div>
<div class="sheet card" style="left:14px;top:128px"><div class="brand"><i></i>KESTREL LANE HEALTH GROUP</div><div class="name">GORDON T PALEY</div><div class="tiny">MANAGER/CEO</div></div>

<!-- letterheads -->
<div class="sheet letter" style="left:150px;top:22px">
  <div class="brand"><i></i>KESTREL LANE HEALTH GROUP</div>
  <p class="body">Dear Client, thank you for your continued trust in our care team. We look forward to serving you again soon.</p>
  <div class="foot">4172 CEDAR HOLLOW RD RENO NEVADA 89511 · www.kestrellanehealth.com</div>
</div>
<div class="sheet letter" style="left:272px;top:22px">
  <div class="brand"><i></i>KESTREL LANE HEALTH GROUP</div>
  <p class="body">Dear Client, thank you for your continued trust in our care team. We look forward to serving you again soon.</p>
  <div class="foot">4172 CEDAR HOLLOW RD RENO NEVADA 89511 · www.kestrellanehealth.com</div>
</div>

<!-- compliment slip and envelopes -->
<div class="sheet dl blue" style="left:396px;top:22px"><div class="brand"><i></i>KESTREL LANE HEALTH GROUP</div></div>
<div class="sheet dl" style="left:396px;top:76px"><div class="brand"><i></i>KESTREL LANE HEALTH GROUP</div><div class="tiny" style="margin-top:8px">With compliments</div><div class="stripe"></div></div>
<div class="sheet dl" style="left:396px;top:130px"><div class="brand"><i></i>KESTREL LANE HEALTH GROUP</div><div class="stripe"></div></div>

<!-- usb sticks -->
<div class="sheet usb" style="left:566px;top:40px"><i></i></div>
<div class="sheet usb" style="left:600px;top:40px"><i></i></div>

<!-- presentation folder -->
<div class="sheet folder" style="left:640px;top:20px"><div class="brand"><i></i>KESTREL LANE HEALTH GROUP</div><div class="tiny" style="position:absolute;bottom:10px">www.kestrellanehealth.com</div></div>
<div class="sheet folder blue" style="left:782px;top:20px;width:130px;display:flex;align-items:center;justify-content:center"><div class="brand"><i></i>KESTREL LANE</div></div>

<!-- disc -->
<div class="sheet cd" style="left:930px;top:36px"></div>

<!-- open folder -->
<div class="sheet blue" style="left:1030px;top:40px;width:76px;height:140px"></div>
<div class="sheet" style="left:1036px;top:110px;width:64px;height:64px;padding:6px"><div class="brand" style="font-size:3.4px"><i style="width:5px;height:5px"></i>KESTREL LANE</div></div>

<!-- screen layouts -->
<div class="sheet" style="left:1120px;top:30px;width:62px;height:80px;padding:5px"><div class="brand" style="font-size:3.4px"><i style="width:5px;height:5px"></i>KESTREL LANE</div><div style="margin-top:8px;height:30px;background:var(--brand)"></div></div>
<div class="sheet blue" style="left:1120px;top:120px;width:62px;height:50px;display:flex;align-items:center;justify-content:center"><div class="brand" style="font-size:3.4px"><i style="width:5px;height:5px"></i>KESTREL LANE</div></div>

</body>
</html>
```